Freight broker online presence/customer portal track shipping

I sleek design showing what we do, broker freight. What we specialize in, chemicals and any freight where domestic or international. We want a home page, a customer portal button on front page that lets clients check on status of their freight (integrate with our transportation management system. Contact page,
Target Market(s)
COMPANIES THAT HAVE PALLETS TO MOVE.
EXAMPLE WEBSITE FROM THE SAME INDUSTRY
https://www.tallowmeadcargo.com/
https://www.pinvelroute.com/
https://www.kdmorrow.com/
Number of Pages Required
3 page

```html
<!DOCTYPE html>
<html lang="en">
<head>
<meta charset="utf-8">
<title>Freight Broker — Home</title>
<link href="https://fonts.googleapis.com/css2?family=Roboto:wght@400;500;700;900&display=swap" rel="stylesheet">
<style>
:root{
  --blue:#2b5aa7;
  --blue-deep:#244f96;
  --teal:#2dab91;
  --red:#e3303e;
  --ink:#151515;
  --body:#555b63;
  --pale:#e8f0f9;
  --white:#ffffff;
}
*{margin:0;padding:0;box-sizing:border-box}
html,body{width:1200px;height:2957px;overflow:hidden}
body{font-family:"Roboto",Arial,sans-serif;color:var(--ink);background:var(--white);position:relative}
.abs{position:absolute}
.btn{position:absolute;display:flex;align-items:center;justify-content:center;background:var(--red);color:var(--white);font-weight:700;font-size:15px;border-radius:32px;text-decoration:none;letter-spacing:-.2px}

/* hero */
.hero{position:absolute;left:0;top:0;width:1200px;height:612px;background:radial-gradient(ellipse at 40% 45%,#2a3b6e 0%,#1a2235 35%,#0e1014 70%),#0e1014}
.hero-road{position:absolute;left:243px;top:430px;width:957px;height:182px;background:linear-gradient(180deg,#2a2722,#3b352c 60%,#24211c)}
.sidebar{position:absolute;left:0;top:0;width:243px;height:612px;background:var(--blue)}
.brand{position:absolute;left:0;top:38px;width:243px;text-align:center;color:var(--white);font-weight:900;line-height:1}
.brand .l1{font-size:52px;letter-spacing:1px}
.brand .l2{font-size:38px;margin-top:6px;letter-spacing:1px}
.side-rule{position:absolute;left:10px;top:182px;width:224px;height:1px;background:rgba(255,255,255,.22)}
.side-nav .item{position:absolute;left:24px;height:43px;display:flex;align-items:center;color:var(--white);font-size:18px;font-weight:500}
.side-nav .item svg{width:22px;height:18px;margin:0 25px 0 19px;fill:var(--white)}
.side-nav .active{background:var(--teal);border-radius:22px;width:146px}
.top-nav{position:absolute;top:40px;left:463px;display:flex;gap:0;color:var(--white);font-size:13px;font-weight:700}
.top-nav span.sep{margin:0 17px;opacity:.9}
.portal{position:absolute;left:877px;top:25px;width:178px;height:47px;border:2px solid var(--red);border-radius:24px;color:var(--white);font-size:13px;font-weight:700;display:flex;align-items:center;justify-content:center}
.hero h1{position:absolute;left:243px;width:957px;text-align:center;top:268px;color:var(--white);font-size:68px;font-weight:900;letter-spacing:-1px;line-height:1}
.hero .lead{position:absolute;left:243px;width:957px;text-align:center;top:358px;color:var(--white);font-size:20px;font-weight:700}

/* what we do */
.what{position:absolute;left:0;top:612px;width:1200px;height:566px}
.what-photo{position:absolute;left:600px;top:0;width:600px;height:566px;background:linear-gradient(135deg,#1d2c48 0%,#2d4670 40%,#6d7a8a 65%,#1a2030 100%)}
h2.sec{font-size:50px;font-weight:900;letter-spacing:-1px;line-height:1}
.para{font-size:13.5px;line-height:28px;color:var(--body)}

/* specialize */
.special{position:absolute;left:0;top:1178px;width:1200px;height:613px;background:var(--teal)}
.card{position:absolute;top:188px;width:290px;height:310px;background:var(--white);clip-path:polygon(0 0,100% 0,100% 278px,258px 100%,0 100%);text-align:center}
.card .pic{position:absolute;left:10px;top:10px;width:270px;height:146px}
.card h3{position:absolute;left:0;width:100%;top:176px;font-size:21px;font-weight:700;color:var(--blue)}
.card p{position:absolute;left:20px;width:250px;top:220px;font-size:13px;line-height:24px;color:var(--body)}
.arrow{position:absolute;top:344px;width:44px;height:44px;border:2px solid var(--white);border-radius:50%}

/* news */
.news-intro{position:absolute;left:0;top:1791px;width:600px;height:381px;background:var(--pale)}
.news-photo{position:absolute;left:0;top:2172px;width:600px;height:349px;background:linear-gradient(180deg,#8ea3bd 0%,#b7c4d3 35%,#2d5a9b 55%,#3b4148 80%,#5b5d5c 100%)}
.post{position:absolute;left:669px;width:420px}
.post h4{font-size:20px;font-weight:500;line-height:28px;color:var(--ink)}
.post .meta{margin-top:9px;font-size:12.5px;color:var(--blue)}
.post .meta span{margin:0 6px}
.post p{margin-top:12px;font-size:13px;line-height:28px;color:#6a6f76}

/* audiences */
.audiences{position:absolute;left:0;top:2521px;width:1200px;height:310px;background:linear-gradient(180deg,#2c5ba8,#2552a0)}
.aud{position:absolute;top:55px;width:260px;text-align:center;color:var(--white)}
.aud svg{width:64px;height:52px;fill:var(--white)}
.aud h5{margin-top:18px;font-size:20px;font-weight:500}
.aud p{margin-top:14px;font-size:13.5px;line-height:24.5px}

/* footer */
.footer{position:absolute;left:0;top:2831px;width:1200px;height:126px;text-align:center}
.footer .legal{position:absolute;top:32px;width:100%;font-size:13px;color:#555}
.social{position:absolute;top:82px;left:0;width:100%;display:flex;justify-content:center;gap:22px}
.social i{display:block;width:24px;height:24px;border-radius:50%;background:var(--blue)}
</style>
</head>
<body>

<header class="hero">
  <div class="hero-road"></div>
  <div class="abs" role="img" aria-label="Night photo of a blue semi truck with trailer on a lit road" style="left:243px;top:0;width:957px;height:612px;background:radial-gradient(ellipse at 25% 55%,rgba(40,60,140,.55),transparent 45%),radial-gradient(ellipse at 95% 45%,rgba(230,180,60,.25),transparent 30%)"></div>

  <aside class="sidebar">
    <div class="brand"><div class="l1">FREIGHT</div><div class="l2">BROKER</div></div>
    <div class="side-rule"></div>
    <nav class="side-nav">
      <div class="item active" style="top:220px"><svg viewBox="0 0 24 20"><path d="M12 1 1 10h3v9h6v-6h4v6h6v-9h3z"/></svg>HOME</div>
      <div class="item" style="top:296px"><svg viewBox="0 0 24 18"><circle cx="12" cy="5" r="4"/><circle cx="4" cy="7" r="3"/><circle cx="20" cy="7" r="3"/><path d="M5 18c0-5 3-7 7-7s7 2 7 7zM0 16c0-4 2-5 4-5 1 0 2 0 3 1-2 1-3 3-3 4zM24 16c0-4-2-5-4-5-1 0-2 0-3 1 2 1 3 3 3 4z"/></svg>ABOUT US</div>
      <div class="item" style="top:372px"><svg viewBox="0 0 24 20"><circle cx="8" cy="11" r="6"/><circle cx="18" cy="5" r="4"/><circle cx="8" cy="11" r="2" fill="#2b5aa7"/><circle cx="18" cy="5" r="1.5" fill="#2b5aa7"/><circle cx="19" cy="15" r="3"/></svg>SERVICES</div>
      <div class="item" style="top:446px"><svg viewBox="0 0 24 20"><path d="M6 0h9l5 5v15H6z"/><path d="M9 10h8M9 13h8M9 16h8" stroke="#2b5aa7" stroke-width="1.4"/></svg>NEWS</div>
      <div class="item" style="top:522px"><svg viewBox="0 0 24 20"><path d="M3 12a9 9 0 0 1 18 0v6h-4v-7h2a7 7 0 0 0-14 0h2v7H3z"/></svg>CONTACT US</div>
    </nav>
  </aside>

  <nav class="top-nav"><span>LOGIN</span><span class="sep">|</span><span>TRACK</span><span class="sep">|</span><span>INVESTORS</span><span class="sep">|</span><span>REQUEST A QUOTE</span></nav>
  <div class="portal">CUSTOMER PORTAL</div>

  <h1>FREIGHT BROKER</h1>
  <div class="lead">Lorem ipsum dolor sit ametconsectetur</div>
  <a class="btn" style="left:630px;top:413px;width:180px;height:60px">GET STARTED</a>
  <svg class="abs" style="left:709px;top:534px" width="22" height="46" viewBox="0 0 22 46" fill="none" stroke="#fff" stroke-width="1.6"><rect x="2" y="1" width="18" height="28" rx="9"/><path d="M11 7v6"/><path d="M4 36l7 6 7-6"/></svg>
</header>

<section class="what">
  <h2 class="sec abs" style="left:145px;top:110px">WHAT WE DO</h2>
  <p class="para abs" style="left:145px;top:186px;width:420px">Lorem ipsum dolor sit amet, consectetur adipiscing esed do eiusmod tempor incididunt ut labore et dolore magna aliquis ipsum suspendisse ultrices gravidus commodo viverra maecenas accumsan lacus vel faciliem ipsum dolor sit amet, consectetur adipiscing eld empor incididunt ut labore et dolore magna s ipsum suspendisse ultrices grdo viverra maecenas accumsan lacus vel facilisis.</p>
  <a class="btn" style="left:145px;top:393px;width:180px;height:60px">READ MORE</a>
  <div class="what-photo" role="img" aria-label="Photo of a person holding a tablet in front of trading screens"></div>
</section>

<section class="special">
  <h2 class="sec abs" style="left:0;width:1200px;text-align:center;top:83px;color:var(--white);font-size:48px">WHAT WE SPECIALIZE IN</h2>
  <svg class="arrow" style="left:72px" viewBox="0 0 44 44" fill="none" stroke="#fff" stroke-width="2.4"><path d="M25 13l-8 9 8 9"/></svg>
  <article class="card" style="left:144px">
    <div class="pic" role="img" aria-label="Photo of a white truck on a highway at sunset" style="background:linear-gradient(180deg,#5a6f8e 0%,#e7b25a 45%,#5a5040 60%,#3a3a3a 100%)"></div>
    <h3>Sed ut perspiciatis</h3>
    <p>Lorem ipsum dolor sit aonsectetur adipiscing elitsed do eiusmod tempor incididunt ut labore</p>
  </article>
  <article class="card" style="left:455px">
    <div class="pic" role="img" aria-label="Aerial photo of a container ship at sea" style="background:linear-gradient(110deg,#0e2530 0%,#163640 35%,#7b4a44 55%,#3d5b78 75%,#b5413f 100%)"></div>
    <h3>Sed quia non nu</h3>
    <p>Lorem ipsum dolor sit aonsectetur adipiscing elitsed do eiusmod tempor incididunt ut labore</p>
  </article>
  <article class="card" style="left:765px">
    <div class="pic" role="img" aria-label="Photo of stacked shipping containers under a red gantry crane" style="background:linear-gradient(180deg,#6f8fc6 0%,#9a4a4e 40%,#3a5a8a 70%,#7a3a3a 100%)"></div>
    <h3>Nemo enim ipsam</h3>
    <p>Lorem ipsum dolor sit aonsectetur adipiscing elitsed do eiusmod tempor incididunt ut labore</p>
  </article>
  <svg class="arrow" style="left:1083px" viewBox="0 0 44 44" fill="none" stroke="#fff" stroke-width="2.4"><path d="M19 13l8 9-8 9"/></svg>
</section>

<section class="news">
  <div class="news-intro">
    <h2 class="sec abs" style="left:96px;top:68px">LATEST NEWS</h2>
    <p class="para abs" style="left:96px;top:152px;width:430px">Lorem ipsum dolor sit amet, consectetur adipiscing esed do eiusmod tempor incididunt ut labore et dolore magna aliquis ipsum suspendisse ultrices gravidus commodo viverra maecenas accumsan</p>
    <a class="btn" style="left:96px;top:267px;width:181px;height:61px">READ MORE</a>
  </div>
  <div class="news-photo" role="img" aria-label="Photo of a blue semi truck with a white trailer under a cloudy sky"></div>

  <article class="post" style="top:1865px">
    <h4>Sed ut perspiciatis unde omnisiste<br>natus errooluptatem</h4>
    <div class="meta">JUNE 28, 2021<span>|</span>Comments</div>
    <p>Lorem ipsum dolor sit amet, consectetur adipiscing eed do eiusmod tempor incididunt ut labore et dolore magna alissuspendisse</p>
  </article>
  <article class="post" style="top:2075px">
    <h4>Sed ut perspiciatis unde omnisiste<br>natus errooluptatem</h4>
    <div class="meta">JUNE 28, 2021<span>|</span>Comments</div>
    <p>Lorem ipsum dolor sit amet, consectetur adipiscing eed do eiusmod tempor incididunt ut labore et dolore magna alissuspendisse</p>
  </article>
  <article class="post" style="top:2285px">
    <h4>Sed ut perspiciatis unde omnisiste<br>natus errooluptatem</h4>
    <div class="meta">JUNE 28, 2021<span>|</span>Comments</div>
    <p>Lorem ipsum dolor sit amet, consectetur adipiscing eed do eiusmod tempor incididunt ut labore et dolore magna alissuspendisse</p>
  </article>
</section>

<section class="audiences" role="img" aria-label="Blue-tinted photo of a logistics office behind three audience columns">
  <div class="aud" style="left:135px">
    <svg viewBox="0 0 64 52"><circle cx="32" cy="12" r="10"/><circle cx="12" cy="17" r="7"/><circle cx="52" cy="17" r="7"/><path d="M14 50c0-14 8-20 18-20s18 6 18 20zM0 46c0-10 5-14 11-14 3 0 5 1 7 2-4 3-6 7-6 12zM64 46c0-10-5-14-11-14-3 0-5 1-7 2 4 3 6 7 6 12z"/></svg>
    <h5>CUSTOMERS</h5>
    <p>Lorem ipsum dolor sit amet, consectetur adipiscing elit, sed do eiusmod tempor incididunt ut labore et dolore magna</p>
  </div>
  <div class="aud" style="left:470px">
    <svg viewBox="0 0 64 52"><path d="M2 4h38v32H2zM42 14h11l9 11v11H42z"/><rect x="47" y="18" width="6" height="7" fill="#2a58a5"/><circle cx="16" cy="41" r="7" stroke="#2a58a5" stroke-width="3"/><circle cx="50" cy="41" r="7" stroke="#2a58a5" stroke-width="3"/></svg>
    <h5>CARRIERS</h5>
    <p>Lorem ipsum dolor sit amet, consectetur adipiscing elit, sed do eiusmod tempor incididunt ut labore et dolore magna</p>
  </div>
  <div class="aud" style="left:803px">
    <svg viewBox="0 0 64 52"><path d="M22 10V4h20v6h-4V8H26v2z"/><rect x="6" y="11" width="52" height="37" rx="4"/><rect x="6" y="27" width="52" height="3" fill="#2a58a5"/><rect x="28" y="24" width="8" height="8" fill="#2a58a5"/></svg>
    <h5>CAREERS</h5>
    <p>Lorem ipsum dolor sit amet, consectetur adipiscing elit, sed do eiusmod tempor incididunt ut labore et dolore magna</p>
  </div>
</section>

<footer class="footer">
  <div class="legal">© 2021 Freight Broker.All Rights Reserved &nbsp;|&nbsp; Privacy Policy | &nbsp;Terms and Conditons</div>
  <div class="social" aria-label="Social links"><i></i><i></i><i></i></div>
</footer>

</body>
</html>
```